HOME IMPROVEMENT Business Card

I want a very unique business card. nothing typical and boring. Im open to you ideas. Ive seen cards with gold and silver or color foil and spot UV coatings. Im looking for something that looks cool and grabs attention. I like rounded corners but am open to all suggestions. We are a home improvement company and I will have a presentation folder printed and a catalog printed also and want to keep that same theme. I love the colors in our logo but I am open at looking at a 3rd color that would work with my logo. I hope that helps.
Card should include
Address
Phone
Fax
Email
Website
Target Market(s)
Home owners, people looking to remodel their home
Industry/Entity Type
Home Improvement
Contact Information for Business Card
2873 Maple Crest Avenue Unit 410
Brookfield Park, Il 60284
Phone
Direct Line
Email
Website
Font styles to use
Other font styles liked:
- IM OPEN MINDED
Requirements
Must have
- High end quality look nothing boring I like rounded corners but am open minded
Nice to have
- WOW. I want something nice and impressive.
Should not have
- ??? Not sure

```html
<!DOCTYPE html>
<html lang="en">
<head>
<meta charset="utf-8">
<title>Hearthline Remodeling Group – Business Card</title>
<link href="https://fonts.googleapis.com/css2?family=Archivo+Narrow:wght@700&family=Montserrat:wght@700;800&family=Oswald:wght@600&display=swap" rel="stylesheet">
<style>
  :root {
    --navy: #0f1240;
    --navy-deep: #080a2a;
    --green: #2db774;
    --white: #ffffff;
    --slogan-grey: #9a9ca8;
    --stripe: #1e1e22;
    --backdrop: #e6e6e3;
  }
  html, body {
    margin: 0;
    padding: 0;
    width: 1200px;
    height: 1135px;
    overflow: hidden;
    background: var(--backdrop);
  }
  .canvas {
    position: relative;
    width: 1200px;
    height: 1135px;
  }
  .card {
    position: absolute;
    left: 260px;
    width: 680px;
    height: 407px;
    box-shadow: 0 10px 28px rgba(0,0,0,0.25);
  }
  .card--front { top: 100px; }
  .card--back { top: 628px; }
  .card svg { display: block; width: 100%; height: 100%; }
  .contact-text {
    font-family: "Archivo Narrow", "Arial Narrow", sans-serif;
    font-weight: 700;
    font-size: 9.5px;
    letter-spacing: 0.5px;
    fill: var(--white);
  }
  .holder-name {
    font-family: "Montserrat", Arial, sans-serif;
    font-weight: 700;
    font-size: 15px;
    letter-spacing: 2.4px;
    fill: var(--white);
  }
  .holder-slogan {
    font-family: "Oswald", "Arial Narrow", sans-serif;
    font-weight: 600;
    font-size: 13px;
    letter-spacing: 1.6px;
    fill: var(--slogan-grey);
  }
  .brand-name {
    font-family: "Montserrat", Arial, sans-serif;
    font-weight: 800;
    font-size: 30px;
    letter-spacing: -0.5px;
    fill: var(--navy);
  }
  .icon-disc { fill: var(--white); }
  .icon-glyph { fill: var(--navy); }
  .icon-stroke { fill: none; stroke: var(--navy); stroke-width: 1.2; }
</style>
</head>
<body>
<main class="canvas">

  <section class="card card--front" aria-label="Business card front">
    <svg viewBox="0 0 543 325" xmlns="http://www.w3.org/2000/svg">
      <rect class="front-base" width="543" height="325" fill="var(--navy)"/>
      <polygon class="front-fold-shadow" points="212,0 232,0 338,190 324,190" fill="var(--navy-deep)"/>
      <polygon class="front-wedge-top" points="448,0 543,0 543,190 332,190" fill="var(--green)"/>
      <rect class="front-name-band" x="0" y="190" width="543" height="87" fill="var(--navy)"/>
      <polygon class="front-wedge-bottom-shadow" points="268,270 275,277 250,325 244,325" fill="var(--navy-deep)"/>
      <polygon class="front-wedge-bottom" points="275,277 543,277 543,325 245,325" fill="var(--green)"/>

      <g class="contact-list">
        <circle class="icon-disc" cx="48" cy="69" r="9"/>
        <rect class="icon-glyph" x="45" y="63.5" width="6" height="11" rx="1.2"/>
        <text class="contact-text" x="67" y="73">5550198</text>

        <circle class="icon-disc" cx="48" cy="102" r="9"/>
        <path class="icon-glyph" d="M44 97.5c0.8-0.8 1.6-0.6 2.1 0.2l1 1.6c0.3 0.6 0.1 1.1-0.4 1.5l-0.6 0.4c0.6 1.4 1.7 2.5 3.1 3.1l0.4-0.6c0.4-0.5 0.9-0.7 1.5-0.4l1.6 1c0.8 0.5 1 1.3 0.2 2.1-1 1-2.6 1.2-4.5 0-2-1.3-3.5-2.8-4.8-4.8-1.2-1.9-1-3.5 0.4-4.1z"/>
        <text class="contact-text" x="67" y="106">555 -0147</text>

        <circle class="icon-disc" cx="48" cy="136" r="9"/>
        <rect class="icon-glyph" x="43" y="132" width="10" height="7.5" rx="1"/>
        <path d="M43.5 132.8l4.5 3.4 4.5-3.4" fill="none" stroke="var(--white)" stroke-width="0.9"/>
        <text class="contact-text" x="67" y="140">info@hearthline.co</text>

        <circle class="icon-disc" cx="48" cy="169" r="9"/>
        <rect class="icon-glyph" x="45.5" y="163.5" width="5" height="3"/>
        <rect class="icon-glyph" x="43" y="166.5" width="10" height="5" rx="1"/>
        <rect class="icon-glyph" x="45.5" y="171" width="5" height="3"/>
        <text class="contact-text" x="67" y="173">555 -0162</text>

        <circle class="icon-disc" cx="48" cy="203" r="9"/>
        <circle class="icon-stroke" cx="48" cy="203" r="4.6"/>
        <ellipse class="icon-stroke" cx="48" cy="203" rx="2" ry="4.6"/>
        <line class="icon-stroke" x1="43.4" y1="203" x2="52.6" y2="203"/>
        <text class="contact-text" x="67" y="207">www.hearthline.co</text>

        <circle class="icon-disc" cx="48" cy="239" r="9"/>
        <path class="icon-glyph" d="M48 245c-2.8-3.4-4-5.4-4-7.2a4 4 0 0 1 8 0c0 1.8-1.2 3.8-4 7.2z"/>
        <circle cx="48" cy="237.8" r="1.4" fill="var(--white)"/>
        <text class="contact-text" x="67" y="242">2873 Maple Crest Avenue Unit 410</text>
        <text class="contact-text" x="67" y="256">Brookfield Park, Il 60284</text>
      </g>

      <text class="holder-name" x="430" y="230" text-anchor="middle">YOUR NAME</text>
      <text class="holder-slogan" x="430" y="254" text-anchor="middle">SLOGAN</text>
    </svg>
  </section>

  <section class="card card--back" aria-label="Business card back">
    <svg viewBox="0 0 543 325" xmlns="http://www.w3.org/2000/svg">
      <defs>
        <linearGradient id="sweep-shadow" x1="0" y1="0" x2="0" y2="1">
          <stop offset="0" stop-color="var(--navy-deep)" stop-opacity="0"/>
          <stop offset="1" stop-color="var(--navy-deep)" stop-opacity="0.55"/>
        </linearGradient>
      </defs>
      <rect class="back-base" width="543" height="325" fill="var(--white)"/>
      <path class="back-top-band" d="M0 0H543V62C420 36 250 60 0 152Z" fill="var(--navy)"/>
      <path class="back-sweep-shadow" d="M0 152C250 60 420 36 543 62V68C420 44 250 66 0 158Z" fill="url(#sweep-shadow)"/>
      <polygon class="back-green-wedge" points="245,182 543,92 543,318" fill="var(--green)"/>
      <rect class="back-base-stripe" x="0" y="302" width="543" height="12" fill="var(--stripe)"/>

      <g class="brand-lockup">
        <rect x="28" y="185" width="13" height="13" fill="var(--green)"/>
        <text class="brand-name" x="48" y="198">Hearthline</text>
      </g>
    </svg>
  </section>

</main>
</body>
</html>
```